Freelance IT consultant - minimalist website

I am an independent IT consultant / contractor with established clients. In many cases I sub-contract through other IT companies when performing work for external clients, in which case I am obliged to adopt these other companies' corporate branding. However I am becoming aware that my personal inclusion / involvement is adding significant value to these 3rd party companies' offerings, making them more attractive to their clients. I would like to capitalise on that value by developing my own "personal brand" - providing a means of distinguishing myself from other companies through whom I sub-contract. I figure a personal website would be a good place to start!

I want a design which evokes concepts of "smart, sensible solutions"; "clean and concise". My "competitors" have a tendency towards jargon, and verbose, often meaningless prose. I would like to position myself as the "go to man" for the solution - pure and simple - once all of the posturing and postulating has been finished. (NB: I've used the tagline "Clearwell" for this project, but I'm receptive to other suggestions!)

Finally (...do you believe that? :-) ) my particular forte is Geographic Information Systems (GIS) and spatial databases. So if a website design can somehow incorporate the idea of maps, or the globe, that'd be brilliant (but keep this subtle - I'm not a cartographer and don't wish to convey that suggestion.) Something that suggests the connection between information and databases with maps and locations, perhaps?

Examples / concepts I like:
"Solution" - this is what I do! Often to ill-described, uncertain problems.
http://brovaquest.org/wp-content/uploads/2013/11/Solution.jpg
http://www.quorvelbridge.com.au/Media/Picture/Solutions.jpg

"Elegant design" - this is what I (like to think I) do :-)
http://qmmdelvaro.files.zenblogly.com/2013/03/nautilus1.png
http://static.pexilbox.com/static/61d329ccf5c162d73102b4ec/t/61d357adf5c11c64d75c9899/1465010548160/Nautilus_Shell.png?format=1000w
Updates

I've added a PDF file with some unstructured thoughts and ideas around what I'm after. I realise I've left this brief quite open-ended - I don't mean to make it difficult. I'm really after some graphic design creative brilliance, more than website technical brilliance. Hope this helps!

I've uploaded an excerpt from my personal CV in a bid to answer some of the ... well, quite reasonable questions I'm receiving about what the hell it is that I actually do! By way of explanation, I didn't upload this information - or indeed, by entire CV - originally, because I really am seeking something more timeless than a "latest CV." As I've indicated, I'm really trying to create a web presence to confirm my right to "be here". I fully expect that any serious customers who visit my site will follow through with a "contact me" action, at which time I will be able to respond with a discussion and/or CV tailored to a particular project. That's what I do. As for the not-so-serious visitors to my site, I'd like them to leave with an affirming nod and the mental note that, they've stumbled upon somebody credible. And if they bookmark the site, all the better! :-) Hope this helps!

Reason: I'd really like a couple of extra days to run these ideas past some friends and colleagues. This is great stuff - but like so many deadlines, this one snuck up a bit quicker than I was expecting!

Target Market(s)

Prospective clients already aware of my existence, seeking confirmation / reassurance of my bona-fides and relevance. Typically government or mainstream business IT procurement staff.

Industry/Entity Type

Contractor

Requirements
Must have
• Simple, clean, timeless (?) design. I want a stable, solid web "presence" but don't expect to have to "work" the site at all. It's a brochure, really. But that doesn't mean it can't be a good one!
Nice to have
• Incorporate new logo (currently subject of a separate ArtMarrow project - no: 482917)
Single page design - (I could be persuaded otherwise, but can't see the need for more than one really!)
Should not have
• Rolling banners, smiling actors / actresses, etc (I have no interest in updating these images!)
Shopping cart, news feeds, blah, blah... This is a static advertising presence only.

```html
<!DOCTYPE html>
<html lang="en">
<head>
<meta charset="utf-8">
<title>Clearwell</title>
<link rel="stylesheet" href="https://fonts.googleapis.com/css2?family=Dosis:wght@300;400;500&family=Pontano+Sans&display=swap">
<style>
  :root {
    --brand-blue: #4a8cbf;
    --ink: #333333;
    --ink-soft: #5a5a5a;
    --hero-top: #1c1c1c;
    --hero-bottom: #3a3a3a;
    --white: #ffffff;
    --muted-amp: #9a9a9a;
    --link-green: #2e8a2e;
    --footer-bg: #e6e5e5;
  }
  * { box-sizing: border-box; margin: 0; padding: 0; }
  html, body { width: 1200px; height: 624px; overflow: hidden; background: var(--white); }
  body { position: relative; font-family: "Pontano Sans", Arial, sans-serif; color: var(--ink); }

  /* Header */
  .site-header { position: absolute; left: 0; top: 0; width: 1200px; height: 55px; background: var(--white); border-bottom: 3.5px solid var(--brand-blue); }
  .brand-name { position: absolute; left: 74px; top: 9px; font-family: "Dosis", sans-serif; font-weight: 400; font-size: 27px; line-height: 34px; color: var(--brand-blue); }
  .main-nav { position: absolute; right: 68px; top: 22px; font-family: "Dosis", sans-serif; font-size: 14.5px; color: var(--ink-soft); }
  .main-nav a { color: var(--ink-soft); text-decoration: none; }
  .main-nav a.is-current { color: var(--brand-blue); }
  .main-nav .sep { margin: 0 5px; }

  /* Hero */
  .hero { position: absolute; left: 0; top: 55px; width: 1200px; height: 407px; background: linear-gradient(180deg, var(--hero-top), var(--hero-bottom)); }
  .hero-title { position: absolute; left: 67px; top: 53px; font-family: "Dosis", sans-serif; font-weight: 300; font-size: 43px; line-height: 52px; text-transform: uppercase; }
  .hero-title .line-accent { color: var(--brand-blue); display: block; }
  .hero-title .line-main { color: var(--white); display: block; }
  .hero-title .amp { color: var(--muted-amp); }
  .hero-text { position: absolute; left: 68px; top: 168px; width: 400px; font-size: 13.6px; line-height: 19.6px; color: var(--white); }
  .hero-button { position: absolute; left: 68px; top: 303px; width: 248px; height: 39px; background: var(--brand-blue); color: var(--white); font-family: "Dosis", sans-serif; font-size: 21px; line-height: 39px; text-align: center; text-transform: uppercase; text-decoration: none; }
  .hero-visual { position: absolute; left: 653px; top: 0; width: 396px; height: 407px; background: radial-gradient(ellipse at 50% 45%, #f2f7f8 0 9%, #6b6b6b 22%, #3a3a3a 60%, #2a2a2a 100%); }

  /* Features */
  .features { position: absolute; left: 0; top: 462px; width: 1200px; height: 123px; }
  .feature { position: absolute; top: 18px; display: flex; }
  .feature-media { width: 140px; height: 80px; border: 1px solid var(--brand-blue); flex: none; }
  .feature-body { margin-left: 13px; width: 200px; }
  .feature-title { font-family: "Dosis", sans-serif; font-weight: 400; font-size: 16px; color: var(--brand-blue); line-height: 18px; white-space: nowrap; }
  .feature-text { font-family: Arial, Helvetica, sans-serif; font-size: 11.5px; line-height: 13px; color: var(--ink); margin-top: 3px; width: 175px; }
  .feature-link { display: block; font-family: "Dosis", sans-serif; font-size: 12px; color: var(--link-green); text-decoration: none; margin-top: 4px; }
  .feature--problem { left: 68px; }
  .feature--problem .feature-link { margin-top: 10px; }
  .feature--smart { left: 436px; }
  .feature--gis { left: 804px; }
  .feature--gis .feature-title { font-size: 14.5px; }
  .media--bulb { background: radial-gradient(circle at 52% 60%, #f3d9a0 0 5%, #8a5a1c 25%, #3a2208 70%); }
  .media--puzzle { background: radial-gradient(circle at 40% 40%, #eef4fb 0 15%, #5a86c4 45%, #1e3f7a 100%); }
  .media--tablet { background: linear-gradient(135deg, #c9d6e2, #f1f4f7 50%, #9fb6cb); }

  /* Footer */
  .site-footer { position: absolute; left: 0; top: 585px; width: 1200px; height: 39px; background: var(--footer-bg); font-size: 12.5px; color: var(--ink); line-height: 39px; }
  .copyright { position: absolute; left: 67px; }
  .footer-nav { position: absolute; right: 69px; }
  .footer-nav a { color: var(--ink); text-decoration: none; }
</style>
</head>
<body>
  <header class="site-header">
    <span class="brand-name">Clearwell</span>
    <nav class="main-nav">
      <a class="is-current" href="#">Home</a><span class="sep">|</span><a href="#">About Me</a><span class="sep">|</span><a href="#">What I Do</a><span class="sep">|</span><a href="#">Contact Me</a>
    </nav>
  </header>

  <section class="hero">
    <h1 class="hero-title">
      <span class="line-accent">A Focused Man</span>
      <span class="line-main"><span class="amp">&amp;</span> Its Approach</span>
    </h1>
    <p class="hero-text">Lorem Ipsum is simply dummy text of the printing and typesetting industry. Lorem Ipsum has been the industry's standard dummy text ever since the 1500s, when an unknown printer took a galley of type and scrambled it to make a type specimen book. It has survived not only five centuries, but also the leap into electronic typesetting, remaining essentially unchanged.</p>
    <a class="hero-button" href="#">Learn More</a>
    <div class="hero-visual" role="img" aria-label="Chalkboard of business sketches around a bright keyhole, with a man in a suit walking toward it"></div>
  </section>

  <section class="features">
    <article class="feature feature--problem">
      <div class="feature-media media--bulb" role="img" aria-label="Glowing light bulb hanging in a dark room"></div>
      <div class="feature-body">
        <h2 class="feature-title">Creative Problem Solving</h2>
        <p class="feature-text">Lorem Ipsum is simply dummy text of the printing &amp; typesetting industry.</p>
        <a class="feature-link" href="#">Read More</a>
      </div>
    </article>
    <article class="feature feature--smart">
      <div class="feature-media media--puzzle" role="img" aria-label="Two hands joining puzzle pieces against a blue light"></div>
      <div class="feature-body">
        <h2 class="feature-title">3S - Smart, Sensible Solutions</h2>
        <p class="feature-text">Lorem Ipsum is simply dummy text of the printing &amp; typesetting industry.</p>
        <a class="feature-link" href="#">Read More</a>
      </div>
    </article>
    <article class="feature feature--gis">
      <div class="feature-media media--tablet" role="img" aria-label="Hands pointing at charts on a tablet on a desk"></div>
      <div class="feature-body">
        <h2 class="feature-title">Geographic Information Systems</h2>
        <p class="feature-text">Lorem Ipsum is simply dummy text of the printing &amp; typesetting industry.</p>
        <a class="feature-link" href="#">Read More</a>
      </div>
    </article>
  </section>

  <footer class="site-footer">
    <span class="copyright">Copyright 2014 Clearwell | All Rights Reserved</span>
    <nav class="footer-nav"><a href="#">Home</a> - <a href="#">About Me</a> - <a href="#">What I Do</a> - <a href="#">Contact me</a></nav>
  </footer>
</body>
</html>
```